Online Greeting Card Marketplace redesign

PennedNotes.com is a two-sided greeting card marketplace. Buyers purchase hand-made cards online, indicating their message. Sellers hand-write the message and mail directly to recipient.

We are getting decent foot traffic but low sales. I'm also not drawing a lot of Card Designers to sell their products. Feedback has been that it's cluttered, boring, and out of date.

I've always enjoyed vibes such as Lana Brookfield and Delia Hartwell. I was going for pale blues and chocolate browns (as can be seen in PennedNotes Friendbook and Chirpline pages).

Attached document is my not-so-great attempt to redesign, which is uninviting and unpolished.

Need a new homepage and a second similar page when shopping (click on any category to see what I mean, e.g. Halloween).
Updates

Industry/Entity Type

Shopping

Requirements
Must have
• I think my logo (stick drawing of a man with an envelope) is what is currently driving a lot of traffic and should stay in the design, pending minor tweaks.

I'll need all the details of the final design to give to the programmers (font styles, color numbers, etc).

Nice to have
• I was thinking of a dotted frame to surround each picture? White Pearl luminescent or a metallic? I just don't know if it works.

```html
<!DOCTYPE html>
<html lang="en">
<head>
<meta charset="utf-8">
<title>PennedNotes.com – Handmade Greeting Cards</title>
<link href="https://fonts.googleapis.com/css2?family=Arimo:wght@400;700&family=Open+Sans:wght@300;400;600&display=swap" rel="stylesheet">
<style>
:root{
  --brown:#5f3d0b;
  --blue:#4a7ec4;
  --blue-text:#3f7bc8;
  --side:#3a3a3a;
  --white:#ffffff;
  --black:#000000;
  --card-line:#d8d8d8;
  --frame:#3b0c0c;
  --gray-text:#8a8a8a;
  --quote:#c8c8c8;
  --ink:#2b2b2b;
}
*{margin:0;padding:0;box-sizing:border-box}
html,body{width:951px;height:1200px;overflow:hidden}
body{position:relative;background:var(--side);font-family:"Arimo",Arial,sans-serif}
.abs{position:absolute}
.top-nav{left:0;top:0;width:951px;height:50px;background:var(--brown);display:flex;justify-content:center;align-items:center;gap:23px;padding-left:12px}
.top-nav a{color:var(--white);font-size:14px;text-decoration:none}
.top-stripe{left:0;top:50px;width:951px;height:10px;background:var(--blue)}
.page{left:98px;top:60px;width:755px;height:908px;background:var(--white)}
.logo-art{left:155px;top:86px;width:310px;height:100px;background:linear-gradient(135deg,#f2f2f2,#dfe7f3);border-radius:4px}
.logo-name{left:155px;top:194px;width:310px;text-align:center;font-family:"Open Sans",sans-serif;font-weight:400;font-size:22px;color:var(--ink)}
.hero-line{font-family:"Open Sans",sans-serif;font-weight:300;white-space:nowrap}
.hero-1{left:540px;top:94px;font-size:20px;color:var(--blue-text)}
.hero-2{left:539px;top:125px;font-size:29px;color:var(--brown);font-weight:400}
.hero-3{left:540px;top:165px;font-size:20px;color:var(--gray-text)}
.hero-btn{top:210px;width:109px;height:33px;background:var(--blue);border:1px solid #3a6aac;color:var(--white);font-family:"Open Sans",sans-serif;font-size:14px;display:flex;align-items:center;justify-content:center}
.btn-sellers{left:544px}
.btn-buyers{left:666px}
.search-bar{left:98px;top:271px;width:755px;height:48px;background:var(--blue)}
.search-input{left:119px;top:278px;width:281px;height:32px;background:var(--white)}
.search-btn{left:400px;top:278px;width:100px;height:32px;background:var(--brown);color:var(--white);font-family:"Open Sans",sans-serif;font-size:16px;font-weight:600;display:flex;align-items:center;justify-content:center}
.search-divider{left:608px;top:275px;width:1px;height:40px;background:#7aa2d6}
.cart{left:639px;top:288px;color:var(--white);font-weight:700;font-size:13px;word-spacing:1px}
.cart span{margin-left:8px}
.sidebar{left:102px;top:325px;width:128px}
.side-title{color:var(--blue-text);font-size:13px;font-weight:400;margin:6px 0 6px 6px}
.side-list{list-style:none;margin:0 0 18px 14px}
.side-list li{font-size:9px;color:#3d2a0e;line-height:14px}
.side-divider{left:235px;top:325px;width:1px;height:640px;background:#e4e4e4}
.side-box{left:102px;top:654px;width:128px;height:303px;background:var(--blue);color:var(--white);padding:10px 9px}
.box-title{font-size:13px;margin-bottom:10px}
.news-text{font-size:8px;line-height:10px;margin-bottom:24px}
.subscribe{display:flex;margin-bottom:36px}
.subscribe-field{width:89px;height:19px;background:var(--white)}
.subscribe-go{width:22px;height:19px;background:#9a9a8a;display:flex;align-items:center;justify-content:center}
.follow-row{display:grid;grid-template-columns:1fr 1fr;gap:5px 4px;margin-top:12px}
.follow-item{display:flex;align-items:center;gap:4px;font-size:8px}
.follow-item i{width:12px;height:12px;background:var(--white);border-radius:2px;display:block;flex:none}
.section-head{left:242px;width:603px;height:39px;background:var(--brown);color:var(--white);font-weight:700;font-size:16px;padding:11px 11px}
.card{width:117px;height:197px;border:1px solid var(--card-line);background:var(--white)}
.card-title{height:36px;margin:0 7px;border-bottom:1px solid var(--card-line);color:var(--blue-text);font-size:11px;font-weight:700;line-height:10px;display:flex;align-items:center;justify-content:center;text-align:center}
.card-photo{display:block;margin:11px auto 0;width:80px;height:92px;border:3px solid var(--frame);background:linear-gradient(160deg,#f1f1f1,#dcdcdc)}
.card-by{margin-top:21px;text-align:center;font-size:9px;color:#3d2a0e}
.card-by b{font-weight:400;color:var(--blue-text);margin-right:4px}
.footer{left:0;top:968px;width:951px;height:176px;background:var(--black)}
.foot-divider{top:985px;width:1px;height:145px;background:#444}
.foot-title{color:var(--blue-text);font-weight:700;font-size:11px}
.quote{left:132px;top:1030px;width:195px;color:var(--quote);font-size:10px;line-height:11px}
.quote-name{left:220px;top:1096px;color:var(--blue-text);font-weight:700;font-size:11px}
.quote-site{left:229px;top:1108px;color:var(--white);font-size:9px}
.social{top:1042px;width:44px;height:44px;border-radius:5px;background:linear-gradient(#f4f4f4,#a9a9a9)}
.social-label{top:1092px;width:70px;text-align:center;color:var(--quote);font-size:9px}
.foot-links{left:664px;top:1006px;color:var(--white);font-size:13px;line-height:18px}
.bottom-bar{left:0;top:1144px;width:951px;height:56px;background:var(--brown)}
.copyright{left:116px;top:1156px;color:var(--white);font-size:11px}
.bottom-links{left:116px;top:1177px;display:flex;gap:16px}
.bottom-links a{color:var(--white);font-size:9px;text-decoration:none}
</style>
</head>
<body>

<nav class="abs top-nav">
  <a href="#">Home</a><a href="#">Contact Us</a><a href="#">About Us</a><a href="#">FAQ</a><a href="#">How It Works</a><a href="#">Terms &amp; Conditions</a><a href="#">Privacy</a>
</nav>
<div class="abs top-stripe"></div>

<div class="abs page"></div>

<div class="abs logo-art" role="img" aria-label="Brand illustration: stick figure man holding a large blue envelope"></div>
<div class="abs logo-name">PennedNotes.com</div>

<div class="abs hero-line hero-1">For Events You</div>
<div class="abs hero-line hero-2">Love to Celebrate</div>
<div class="abs hero-line hero-3">With Your Love One</div>
<div class="abs hero-btn btn-sellers">For Sellers</div>
<div class="abs hero-btn btn-buyers">For Buyers</div>

<div class="abs search-bar"></div>
<div class="abs search-input"></div>
<div class="abs search-btn">Search</div>
<div class="abs search-divider"></div>
<div class="abs cart">Shopping Cart:<span>2 Items</span></div>

<aside class="abs sidebar">
  <h3 class="side-title">Upcoming Holidays</h3>
  <ul class="side-list"><li>Columbus Day</li><li>Halloween</li><li>Veteran's Day</li><li>Thanksgiving Day</li><li>Hanukkah</li></ul>
  <h3 class="side-title">Birthday Cards</h3>
  <ul class="side-list"><li>Kids Birthday</li><li>His Birthday</li><li>Her Birthday</li><li>Family Birthday</li><li>General Birthday</li></ul>
  <h3 class="side-title">Everyday Cards</h3>
  <ul class="side-list"><li>Sympathy</li><li>Graduation</li><li>Baby</li><li>Anniversary</li><li>Thank You</li></ul>
</aside>
<div class="abs side-divider"></div>

<div class="abs side-box">
  <div class="box-title">Corporate News</div>
  <p class="news-text">What a great honor to be a featured artist for the Makers Women's Circle. Please take a moment to read the article about PennedNotes founder. Thank you MWC! Click Here to Read the full Article.</p>
  <div class="box-title">Subscribe</div>
  <div class="subscribe"><div class="subscribe-field"></div><div class="subscribe-go"><svg width="8" height="9" viewBox="0 0 8 9"><path d="M0 0L8 4.5L0 9Z" fill="#fff"/></svg></div></div>
  <div class="box-title">Follow Us</div>
  <div class="follow-row">
    <div class="follow-item"><i></i>Friendbook</div>
    <div class="follow-item"><i></i>Pinwall</div>
    <div class="follow-item"><i></i>Chirpline</div>
    <div class="follow-item"><i></i>Feed</div>
  </div>
</div>

<h2 class="abs section-head" style="top:326px">Best Selling Cards</h2>
<div class="abs card" style="left:242px;top:376px"><div class="card-title">So Sweet</div><div class="card-photo" role="img" aria-label="Handmade card with flower basket"></div><div class="card-by"><b>By:</b>Penned Notes</div></div>
<div class="abs card" style="left:364px;top:376px"><div class="card-title">Quilled Button Flowers</div><div class="card-photo" role="img" aria-label="Handmade card with flower basket"></div><div class="card-by"><b>By:</b>Penned Notes</div></div>
<div class="abs card" style="left:485px;top:376px"><div class="card-title">So Sweet</div><div class="card-photo" role="img" aria-label="Handmade card with flower basket"></div><div class="card-by"><b>By:</b>Penned Notes</div></div>
<div class="abs card" style="left:607px;top:376px"><div class="card-title">Quilled Button Flowers</div><div class="card-photo" role="img" aria-label="Handmade card with flower basket"></div><div class="card-by"><b>By:</b>Penned Notes</div></div>
<div class="abs card" style="left:728px;top:376px"><div class="card-title">So Sweet</div><div class="card-photo" role="img" aria-label="Handmade card with flower basket"></div><div class="card-by"><b>By:</b>Penned Notes</div></div>

<h2 class="abs section-head" style="top:583px">Best Selling Cards</h2>
<div class="abs card" style="left:242px;top:633px"><div class="card-title">So Sweet</div><div class="card-photo" role="img" aria-label="Handmade card with flower basket"></div><div class="card-by"><b>By:</b>Penned Notes</div></div>
<div class="abs card" style="left:364px;top:633px"><div class="card-title">Quilled Button Flowers</div><div class="card-photo" role="img" aria-label="Handmade card with flower basket"></div><div class="card-by"><b>By:</b>Penned Notes</div></div>
<div class="abs card" style="left:485px;top:633px"><div class="card-title">So Sweet</div><div class="card-photo" role="img" aria-label="Handmade card with flower basket"></div><div class="card-by"><b>By:</b>Penned Notes</div></div>
<div class="abs card" style="left:607px;top:633px"><div class="card-title">Quilled Button Flowers</div><div class="card-photo" role="img" aria-label="Handmade card with flower basket"></div><div class="card-by"><b>By:</b>Penned Notes</div></div>
<div class="abs card" style="left:728px;top:633px"><div class="card-title">So Sweet</div><div class="card-photo" role="img" aria-label="Handmade card with flower basket"></div><div class="card-by"><b>By:</b>Penned Notes</div></div>

<footer class="abs footer"></footer>
<div class="abs foot-divider" style="left:354px"></div>
<div class="abs foot-divider" style="left:628px"></div>
<div class="abs foot-title" style="left:125px;top:999px">What People Are Saying About Us</div>
<p class="abs quote">They are simply amazing, i run my site within 3 days after order and getting on sales rightaway</p>
<div class="abs quote-name">Rina Castellan</div>
<div class="abs quote-site">www.samplestore.net</div>
<div class="abs foot-title" style="left:403px;top:999px;font-size:12px">Follow Us</div>
<div class="abs social" style="left:406px" aria-label="Circlespace"></div>
<div class="abs social" style="left:477px" aria-label="Friendbook"></div>
<div class="abs social" style="left:550px" aria-label="Chirpline"></div>
<div class="abs social-label" style="left:393px">Circlespace</div>
<div class="abs social-label" style="left:464px">Friendbook</div>
<div class="abs social-label" style="left:537px">Chirpline</div>
<div class="abs foot-links">Frequently Asked Questions<br>Contact Us<br>Get Started</div>

<div class="abs bottom-bar"></div>
<div class="abs copyright">Copyright All Rights Reserved</div>
<nav class="abs bottom-links">
  <a href="#">Home</a><a href="#">Contact Us</a><a href="#">About Us</a><a href="#">FAQ</a><a href="#">How It Works</a><a href="#">Terms &amp; Conditions</a><a href="#">Privacy</a>
</nav>

</body>
</html>
```